BRIGHTVALE ADVISERS POWERPOINT PRESENTATION TEMPLATE 1

We need the ultimate quality Powerpoint presentation design.
We are the advisory firm working with modern world class tech companies throughout Europe, their founders, shareholders, and potential investors.
The new template must contain elements such as our logo, appropriate backgrounds, be at the same time very attractive visually and easy to rear. Also there must be some place where logo of our clients should be placed.

We like:
- icons and
- infographics,
so attractive design in this area will be greatly appreciated.

Please avoid serif fonts and excessive decorations such as "waves" or other similar decor.

We are also in contact with serious investors - wealthy individuals, reputable financial institutions, and their advisers; banks, private equity investors, global technology companies.

The Powerpoint template design must send a message that:
- we are a high technology oriented team of professionals,
- we provide modern financial advisory services
- but at the same time we are open minded, creative, yet very competent in the area of corporate finance.

The Powerpoint template must complement our business card design, first impression of a team of top notch professionals who advise top notch tech companies on their top notch corporate finance and M&A projects.

Enclosed are sets of our logo, current template, business card project which won previous competition.

It is perhaps a good basis to start with and get us to the template of our dreams.

While working on this project please think about the following firms which at some point may be looking at your design:
- Quorlin
- Tavindex
- Pelorim
- Veskaran (Zundle)
- Marowisp
- Turnequo
- Dovrash
- Kelvaro
- Obrethy

The quality of the design, its style, aesthetics must meet the top criteria in contemporary design trends.

Target Market(s)

Banks, financial investors, strategic investors

Industry/Entity Type

Finance

Font styles to use
Sans Serif

Requirements
Must have
• Icons
Infographics
Attractive backgrounds
Clean design
Harmonize with logo and emblem colors.
Should not have
• Excessive tacky decor (waves, etc)
Serif fonts
Excessive colors

```html
<!DOCTYPE html>
<html lang="en">
<head>
<meta charset="utf-8">
<title>Brightvale Business PowerPoint Template – Sample Slides</title>
<link rel="stylesheet" href="https://fonts.googleapis.com/css2?family=Barlow:wght@400;500;600;700&family=Open+Sans:wght@300;400&display=swap">
<style>
:root{
  --page:#0e1830;
  --navy:#1b2d5a;
  --blue:#1f4c99;
  --blue-mid:#2d6fc4;
  --heading-blue:#1f4f9a;
  --ink:#1b2433;
  --muted:#5a6576;
  --red:#d8322c;
  --green:#4fe0a0;
  --light-a:#d3d9e2;
  --light-b:#eef1f5;
  --white:#ffffff;
}
*{margin:0;padding:0;box-sizing:border-box}
html,body{width:667px;height:1200px;overflow:hidden;background:var(--page)}
body{font-family:"Barlow",Arial,sans-serif;color:var(--ink);position:relative}
.icon-defs{position:absolute;width:0;height:0}
.sheet-title{position:absolute;top:24px;left:0;width:667px;text-align:center;font-family:"Open Sans",Arial,sans-serif;font-weight:400;font-size:25px;color:var(--white)}
.sheet-sub{position:absolute;top:62px;left:0;width:667px;text-align:center;font-family:"Open Sans",Arial,sans-serif;font-weight:300;font-size:18px;color:#c8cfdb}
.slide{position:absolute;width:304px;height:171px;overflow:hidden;background:linear-gradient(180deg,var(--light-a),var(--light-b))}
.slide.dark{background:linear-gradient(180deg,var(--navy),var(--blue));color:var(--white)}
.col-l{left:27px}.col-r{left:336px}
.r1{top:105px}.r2{top:281px}.r3{top:457px}.r4{top:634px}.r5{top:810px}.r6{top:986px}
.abs{position:absolute}
svg.layer{position:absolute;left:0;top:0}
.kicker{position:absolute;top:8px;left:17px;font-size:3px;color:var(--muted)}
.dark .kicker{color:#c4cde0}
.rule{position:absolute;top:12.5px;left:17px;right:17px;height:.4px;background:#9aa6b6}
.rule::after{content:"";position:absolute;right:0;top:-.3px;width:10px;height:1px;background:var(--blue-mid)}
.conf{position:absolute;top:3px;right:17px;font-size:2.4px;font-weight:700;color:var(--red)}
.dark .conf{color:var(--white)}
.s-title{position:absolute;top:18px;left:17px;font-size:6.8px;font-weight:700}
.s-sub{position:absolute;top:28px;left:17px;font-size:4.2px;color:#394454}
.dark .s-sub{color:#d9e0ee}
.foot{position:absolute;left:0;bottom:0;width:100%;height:10px;background:var(--white)}
.foot .src{position:absolute;left:17px;top:3.5px;font-size:2.6px;color:#8a94a3}
.foot .src::before{content:"";position:absolute;left:0;top:-2px;width:18px;height:.8px;background:var(--blue-mid)}
.foot .mark{position:absolute;right:25px;top:2.6px;display:flex;align-items:center;gap:1.5px;font-size:3.4px;font-weight:600;color:var(--heading-blue)}
.foot .num{position:absolute;right:17px;top:3.5px;font-size:2.4px;color:#8a94a3}
.dot{display:inline-block;border-radius:50%;background:var(--heading-blue)}
.foot .dot{width:4px;height:4px}
.lorem{font-size:3px;line-height:1.3;color:#3b4656}
.lorem.c{text-align:center}
.hd{font-size:3.5px;font-weight:700;color:var(--heading-blue)}
.body3{font-size:3.3px;line-height:1.3;color:#3b4656}
.key{font-size:6px;font-weight:700;line-height:1.25;color:var(--heading-blue)}
.dark .key{color:var(--white)}
.key-body{font-size:3.8px;line-height:1.3;color:#3b4656;margin-top:2px}
.dark .key-body{color:#dde4f2}
.cover{background:var(--white)}
.cover .brand{position:absolute;left:15px;top:73px;display:flex;align-items:center;gap:3px;font-size:8px;font-weight:500;color:var(--heading-blue)}
.cover .brand .dot{width:9px;height:9px}
.cover h1{position:absolute;left:15px;top:102px;font-size:10px;line-height:1.2;font-weight:700;color:var(--heading-blue)}
.cover .lede{position:absolute;left:15px;top:132px;font-size:6px;color:#8c96a6}
.toc{background:var(--blue)}
.toc h2{position:absolute;left:16px;top:20px;font-size:8.5px;font-weight:700;line-height:1.2;color:var(--white)}
.toc .part{position:absolute;color:var(--white);width:62px}
.toc .roman{display:inline-block;width:6px;height:6px;border:.4px solid #fff;border-radius:50%;font-size:3px;text-align:center;line-height:5.4px}
.toc .ph{font-size:4.3px;font-weight:700;margin:1.5px 0;line-height:1.15}
.toc ol{list-style:none;font-size:2.8px;line-height:1.6;color:#d4def0}
.fact{position:absolute;width:50px}
.fact .n{font-family:"Open Sans",Arial,sans-serif;font-weight:300;font-size:12px;color:var(--white);line-height:1}
.fact .n small{font-size:8px}
.fact .t{font-size:2.8px;line-height:1.3;color:#d2dbec;margin-top:2px}
.thanks{background:var(--navy)}
.thanks .msg{position:absolute;left:17px;top:82px;font-family:"Open Sans",Arial,sans-serif;font-weight:300;font-size:22px;color:#c9d1de}
.thanks .brand{position:absolute;left:20px;top:133px;text-align:center;font-size:5.5px;font-weight:500;color:var(--white)}
.thanks .brand .dot{display:block;margin:0 auto 2px;width:8px;height:8px;background:var(--white)}
</style>
</head>
<body>

<svg class="icon-defs" aria-hidden="true">
  <defs>
    <symbol id="i-doc" viewBox="0 0 10 10"><g fill="none" stroke="currentColor" stroke-width=".7" stroke-linejoin="round"><rect x="1" y="1.5" width="6" height="7.5"/><path d="M3 1.5v-1h2v1M2.5 4h3M2.5 5.5h3M2.5 7h1.5"/><path d="M5.5 8.5l3.5-3.5 .8 .8-3.5 3.5h-.8z" stroke="#3fcf8e"/></g></symbol>
    <symbol id="i-bldg" viewBox="0 0 10 10"><g fill="none" stroke="currentColor" stroke-width=".7"><rect x="2" y="1.5" width="4.5" height="7.5"/><rect x="6.5" y="4.5" width="2.5" height="4.5"/><path d="M3 3h.8M4.7 3h.8M3 4.6h.8M4.7 4.6h.8M3 6.2h.8M4.7 6.2h.8M1 9h9"/><path d="M7.3 6h1" stroke="#3fcf8e"/></g></symbol>
    <symbol id="i-board" viewBox="0 0 10 10"><g fill="none" stroke="currentColor" stroke-width=".7"><rect x="1" y="1.5" width="8" height="5"/><path d="M5 6.5v2M3 9l2-1 2 1"/><path d="M2.3 5.2l1.8-1.6 1.4 1 2.2-1.8" stroke="#3fcf8e"/></g></symbol>
    <symbol id="i-grow" viewBox="0 0 10 10"><g fill="none" stroke="currentColor" stroke-width=".7"><path d="M1 8.5h3.5l2-1.3h2.5"/><path d="M5 7.2v-3"/><path d="M5 4.8c-1.8 0-2.5-1-2.5-2.3 1.5 0 2.5.8 2.5 2.3zM5 4.2c0-1.6 1-2.6 2.7-2.6 0 1.6-1 2.6-2.7 2.6z" stroke="#3fcf8e"/></g></symbol>
    <symbol id="i-team" viewBox="0 0 10 10"><g fill="none" stroke="currentColor" stroke-width=".7"><rect x="1" y="1" width="8" height="5"/><circle cx="3.5" cy="7.3" r=".8"/><circle cx="6.5" cy="7.3" r=".8"/><path d="M2 9.5c.3-.9 2.7-.9 3 0M5 9.5c.3-.9 2.7-.9 3 0"/><path d="M3 4.5l1.5-1.5 1.2 1 1.5-1.5" stroke="#3fcf8e"/></g></symbol>
    <symbol id="i-gear" viewBox="0 0 10 10"><g fill="none" stroke="currentColor" stroke-width=".7"><circle cx="5" cy="4" r="2.2"/><path d="M5 .8v1M5 6.2v1M1.8 4h1M7.2 4h1"/><path d="M2 9.3c.4-1.3 1.6-1.9 3-1.9s2.6.6 3 1.9"/><circle cx="5" cy="4" r=".7" stroke="#3fcf8e"/></g></symbol>
    <symbol id="i-search" viewBox="0 0 10 10"><g fill="none" stroke="currentColor" stroke-width=".7"><circle cx="4.2" cy="4.2" r="2.8"/><path d="M6.3 6.3l2.7 2.7"/><path d="M3 4.2h2.4M4.2 3v2.4" stroke="#3fcf8e"/></g></symbol>
    <symbol id="i-money" viewBox="0 0 10 10"><g fill="none" stroke="currentColor" stroke-width=".7"><rect x="1" y="1" width="5.5" height="7.5"/><path d="M2.2 3h3M2.2 4.5h3M2.2 6h1.5"/><circle cx="7" cy="7" r="2" stroke="#3fcf8e"/></g></symbol>
  </defs>
</svg>

<div class="sheet-title">BRIGHTVALE BUSINESS POWERPOINT TEMPLATE</div>
<div class="sheet-sub">SAMPLE SLIDES</div>

<!-- 1 cover -->
<section class="slide cover col-l r1">
  <svg class="layer" width="304" height="171" viewBox="0 0 304 171" role="img" aria-label="Misty city skyline photograph in blue tones behind diagonal panels">
    <defs>
      <linearGradient id="coverSky" x1="0" y1="0" x2="1" y2="1"><stop offset="0" stop-color="#c9d3df"/><stop offset=".55" stop-color="#8da3bd"/><stop offset="1" stop-color="#4a6f9e"/></linearGradient>
      <linearGradient id="coverBlue" x1="0" y1="0" x2="0" y2="1"><stop offset="0" stop-color="#4d7fc2"/><stop offset="1" stop-color="#2a5ea8"/></linearGradient>
    </defs>
    <polygon points="0,0 304,0 304,171 138,171 175,100" fill="url(#coverSky)"/>
    <polygon points="230,0 304,0 304,171 170,171" fill="url(#coverBlue)" opacity=".85"/>
    <polygon points="232,171 250,140 304,171" fill="#ffffff"/>
    <polygon points="224,171 235,158 246,171" fill="#7aa33a"/>
  </svg>
  <div class="brand"><span class="dot"></span>BRIGHTVALE</div>
  <h1>Enter presentation<br>title here</h1>
  <div class="lede">Subtitle here or speaker name</div>
</section>

<!-- 2 table of contents -->
<section class="slide toc col-r r1">
  <svg class="layer" width="74" height="171" viewBox="0 0 74 171" role="img" aria-label="Office interior photograph overlooking a city in deep blue">
    <defs><linearGradient id="tocPhoto" x1="0" y1="0" x2="0" y2="1"><stop offset="0" stop-color="#2f4f86"/><stop offset=".6" stop-color="#1c3565"/><stop offset="1" stop-color="#0f1f40"/></linearGradient></defs>
    <rect width="74" height="171" fill="url(#tocPhoto)"/>
  </svg>
  <h2>TABLE OF<br>CONTENTS</h2>
  <div class="part" style="left:90px;top:18px"><span class="roman">I</span><div class="ph">Introduction</div>
    <ol><li>1. Introduction</li><li>2. Basic Information</li><li>3. Business development</li><li>4. Development plans</li><li>5. Investment thesis</li></ol></div>
  <div class="part" style="left:155px;top:18px;width:72px"><span class="roman">II</span><div class="ph">Company operations</div>
    <ol><li>1. Product portfolio I</li><li>2. Product description</li><li>3. Production sites</li><li>4. Licenses and certificates</li><li>5. Business model</li><li>6. Marketing strategy</li><li>7. Customer groups</li><li>8. Sales structure</li><li>9. Key Suppliers and Business Partners</li><li>10. Raw Materials</li><li>11. Key people and Organisational structure</li></ol></div>
  <div class="part" style="left:230px;top:18px"><span class="roman">III</span><div class="ph">Market and competition</div>
    <ol><li>1. Market overview</li><li>2. Market competition</li><li>3. Company's competitive advantages</li></ol></div>
  <div class="part" style="left:90px;top:96px;width:46px"><span class="roman">IV</span><div class="ph">Strategy and development plans</div>
    <ol><li>1. Strategy and development plan</li><li>2. Acquisition opportunities</li><li>3. Value proposition</li><li>4. SWOT analysis</li><li>5. Capex and investment effects</li></ol></div>
  <div class="part" style="left:155px;top:96px;width:60px"><span class="roman">V</span><div class="ph">Financial information and forecasts</div>
    <ol><li>1. Income Statement</li><li>2. Revenues structure</li><li>3. Operating costs</li><li>4. Cost of Goods Sold</li><li>5. Sales profitability</li><li>6. Cash Flow Statement</li><li>7. Planned CAPEX</li><li>8. Balance Sheet</li></ol></div>
  <div class="part" style="left:230px;top:96px"><span class="roman">VI</span><div class="ph">Attachments</div>
    <ol><li>1. Financial Statements</li><li>2. Glossary</li></ol></div>
</section>

<!-- 3 timeline -->
<section class="slide col-l r2">
  <div class="kicker">Infographic layouts</div><div class="rule"></div><div class="conf">STRICTLY CONFIDENTIAL</div>
  <div class="s-title">Timeline infographic</div><div class="s-sub">Simple time line with four colors</div>
  <svg class="layer" width="304" height="171" viewBox="0 0 304 171" style="color:#1b2433">
    <g fill="none" stroke-width="3.6">
      <circle cx="46" cy="89" r="13" stroke="#5b8fd0"/><circle cx="76" cy="89" r="13" stroke="#3d5a9c"/>
      <circle cx="106" cy="89" r="13" stroke="#a9b4c1"/><circle cx="136" cy="89" r="13" stroke="#8567b3"/>
      <circle cx="166" cy="89" r="13" stroke="#4a8fd8"/><circle cx="196" cy="89" r="13" stroke="#4fe0a0"/>
      <circle cx="226" cy="89" r="13" stroke="#98c98a"/><circle cx="256" cy="89" r="13" stroke="#8567b3"/>
    </g>
    <g fill="#ffffff" stroke="#dfe4ea" stroke-width=".6">
      <circle cx="46" cy="89" r="9.5"/><circle cx="76" cy="89" r="9.5"/><circle cx="106" cy="89" r="9.5"/><circle cx="136" cy="89" r="9.5"/>
      <circle cx="166" cy="89" r="9.5"/><circle cx="196" cy="89" r="9.5"/><circle cx="226" cy="89" r="9.5"/><circle cx="256" cy="89" r="9.5"/>
    </g>
    <use href="#i-doc" x="41.5" y="84.5" width="9" height="9"/>
    <use href="#i-bldg" x="71.5" y="84.5" width="9" height="9"/>
    <use href="#i-money" x="101.5" y="84.5" width="9" height="9"/>
    <use href="#i-grow" x="131.5" y="84.5" width="9" height="9"/>
    <use href="#i-team" x="161.5" y="84.5" width="9" height="9"/>
    <use href="#i-gear" x="191.5" y="84.5" width="9" height="9"/>
    <use href="#i-search" x="221.5" y="84.5" width="9" height="9"/>
    <use href="#i-money" x="251.5" y="84.5" width="9" height="9"/>
    <g stroke="#7b8594" stroke-width=".3">
      <line x1="46" y1="68" x2="46" y2="76"/><line x1="106" y1="68" x2="106" y2="76"/><line x1="166" y1="68" x2="166" y2="76"/><line x1="226" y1="68" x2="226" y2="76"/>
      <line x1="76" y1="102" x2="76" y2="110"/><line x1="136" y1="102" x2="136" y2="110"/><line x1="196" y1="102" x2="196" y2="110"/><line x1="256" y1="102" x2="256" y2="110"/>
    </g>
  </svg>
  <div class="abs lorem c" style="left:28px;top:55px;width:38px">Lorem Ipsum is simply dummy text of the printing and typesetting industry.</div>
  <div class="abs lorem c" style="left:88px;top:55px;width:38px">Lorem Ipsum is simply dummy text of the printing and typesetting industry.</div>
  <div class="abs lorem c" style="left:148px;top:55px;width:38px">Lorem Ipsum is simply dummy text of the printing and typesetting industry.</div>
  <div class="abs lorem c" style="left:208px;top:55px;width:38px">Lorem Ipsum is simply dummy text of the printing and typesetting industry.</div>
  <div class="abs lorem c" style="left:57px;top:118px;width:38px">Lorem Ipsum is simply dummy text of the printing and typesetting industry.</div>
  <div class="abs lorem c" style="left:117px;top:118px;width:38px">Lorem Ipsum is simply dummy text of the printing and typesetting industry.</div>
  <div class="abs lorem c" style="left:177px;top:118px;width:38px">Lorem Ipsum is simply dummy text of the printing and typesetting industry.</div>
  <div class="abs lorem c" style="left:237px;top:118px;width:38px">Lorem Ipsum is simply dummy text of the printing and typesetting industry.</div>
  <div class="foot"><span class="src">Source here if needed</span><span class="mark"><span class="dot"></span>BRIGHTVALE</span><span class="num">3</span></div>
</section>

<!-- 4 business model -->
<section class="slide col-r r2">
  <div class="kicker">Infographic layouts</div><div class="rule"></div><div class="conf">STRICTLY CONFIDENTIAL</div>
  <div class="s-title">Business model infographic</div><div class="s-sub">Sample model with framework and contents with icons as tracker</div>
  <svg class="layer" width="304" height="171" viewBox="0 0 304 171" style="color:#1b2433">
    <circle cx="61" cy="96" r="22" fill="none" stroke="#a9b4c1" stroke-width=".4" stroke-dasharray="1 1"/>
    <g fill="#ffffff" stroke="#d1d8e1" stroke-width=".6">
      <circle cx="61" cy="61" r="12.5"/><circle cx="94" cy="85" r="12.5"/><circle cx="81" cy="124" r="12.5"/><circle cx="41" cy="124" r="12.5"/><circle cx="28" cy="85" r="12.5"/>
    </g>
    <g fill="none" stroke-width="2.2" stroke-linecap="round">
      <path d="M77 62 q8 2 10 9" stroke="#4fe0a0"/><path d="M95 101 q-1 8 -6 12" stroke="#8567b3"/>
      <path d="M66 132 q-6 3 -12 1" stroke="#98c98a"/><path d="M28 101 q1 7 5 10" stroke="#5b8fd0"/><path d="M46 57 q-7 1 -11 7" stroke="#3d5a9c"/>
    </g>
    <use href="#i-doc" x="56" y="56" width="10" height="10"/>
    <use href="#i-team" x="89" y="80" width="10" height="10"/>
    <use href="#i-grow" x="76" y="119" width="10" height="10"/>
    <use href="#i-money" x="36" y="119" width="10" height="10"/>
    <use href="#i-bldg" x="23" y="80" width="10" height="10"/>
    <use href="#i-doc" x="129" y="44" width="9" height="9"/>
    <use href="#i-team" x="185" y="44" width="9" height="9"/>
    <use href="#i-gear" x="241" y="44" width="9" height="9"/>
    <use href="#i-money" x="129" y="101" width="9" height="9"/>
    <use href="#i-bldg" x="185" y="101" width="9" height="9"/>
  </svg>
  <div class="abs" style="left:50px;top:88px;width:22px;text-align:center;font-size:4.2px;font-weight:600;line-height:1.2;color:var(--heading-blue)">Main Heading Here</div>
  <div class="abs" style="left:129px;top:60px;width:48px"><div class="hd">Heading here</div><div class="body3">Lorem Ipsum is simply dummy text of the printing and typesetting industry.</div></div>
  <div class="abs" style="left:185px;top:60px;width:48px"><div class="hd">Heading here</div><div class="body3">Lorem Ipsum is simply dummy text of the printing and typesetting industry.</div></div>
  <div class="abs" style="left:241px;top:60px;width:48px"><div class="hd">Heading here</div><div class="body3">Lorem Ipsum is simply dummy text of the printing and typesetting industry.</div></div>
  <div class="abs" style="left:129px;top:117px;width:48px"><div class="hd">Heading here</div><div class="body3">Lorem Ipsum is simply dummy text of the printing and typesetting industry.</div></div>
  <div class="abs" style="left:185px;top:117px;width:48px"><div class="hd">Heading here</div><div class="body3">Lorem Ipsum is simply dummy text of the printing and typesetting industry.</div></div>
  <div class="foot"><span class="src">Source here if needed</span><span class="mark"><span class="dot"></span>BRIGHTVALE</span><span class="num">4</span></div>
</section>

<!-- 5 chart -->
<section class="slide dark col-l r3">
  <div class="kicker">Infographic layouts</div><div class="rule"></div><div class="conf">STRICTLY CONFIDENTIAL</div>
  <div class="s-title">Chart infographic</div><div class="s-sub">Sample subtitle</div>
  <svg class="layer" width="304" height="171" viewBox="0 0 304 171">
    <defs><linearGradient id="ringGrad" x1="0" y1="0" x2="0" y2="1"><stop offset="0" stop-color="#2d7fd0"/><stop offset="1" stop-color="#3ff0a0"/></linearGradient></defs>
    <circle cx="62" cy="95" r="50" fill="none" stroke="#ffffff" stroke-width="1.2"/>
    <circle cx="62" cy="95" r="50" fill="none" stroke="url(#ringGrad)" stroke-width="4" stroke-dasharray="204 314" transform="rotate(-90 62 95)"/>
    <circle cx="162" cy="103" r="32" fill="none" stroke="#ffffff" stroke-width="1.2"/>
    <circle cx="162" cy="103" r="32" fill="none" stroke="url(#ringGrad)" stroke-width="3" stroke-dasharray="50 201" transform="rotate(-90 162 103)"/>
    <path d="M229 75l3 4-3 4" fill="none" stroke="#7fd04a" stroke-width="2.2"/>
  </svg>
  <div class="abs" style="left:30px;top:75px;width:64px;text-align:center">
    <div style="font-family:'Open Sans',Arial,sans-serif;font-weight:300;font-size:28px;line-height:1">65<span style="font-size:15px;vertical-align:top">%</span></div>
    <div style="font-size:4px;line-height:1.3;margin-top:1px">Lorem Ipsum is simply dummy text of the printing and typesetting industry.</div>
  </div>
  <div class="abs" style="left:139px;top:91px;width:46px;text-align:center">
    <div style="font-family:'Open Sans',Arial,sans-serif;font-weight:300;font-size:15px;line-height:1">25<span style="font-size:8px;vertical-align:top">%</span></div>
    <div style="font-size:3px;line-height:1.3;margin-top:1px">Lorem Ipsum is simply dummy text of the printing and typesetting industry.</div>
  </div>
  <div class="abs" style="left:242px;top:72px;width:46px"><div class="key">Some key messages here in this format</div><div class="key-body">Lorem Ipsum is simply dummy text of the printing and typesetting industry.</div></div>
  <div class="foot"><span class="src">Source here if needed</span><span class="mark"><span class="dot"></span>BRIGHTVALE</span><span class="num">5</span></div>
</section>

<!-- 6 map -->
<section class="slide col-r r3">
  <div class="kicker">Infographic layouts</div><div class="rule"></div><div class="conf">STRICTLY CONFIDENTIAL</div>
  <div class="s-title">Map infographic</div><div class="s-sub">Sample subtitle</div>
  <svg class="layer" width="304" height="171" viewBox="0 0 304 171" style="color:#1b2433">
    <rect x="18" y="44" width="162" height="102" rx="20" fill="#f4f6f9" opacity=".7" role="img" aria-label="World map in light grey"/>
    <g fill="#ffffff" stroke-width="2">
      <circle cx="48" cy="83" r="6.5" stroke="#5b8fd0"/><circle cx="106" cy="58" r="6.5" stroke="#8567b3"/>
      <circle cx="151" cy="89" r="6.5" stroke="#98c98a"/><circle cx="107" cy="121" r="6.5" stroke="#4fe0a0"/><circle cx="61" cy="135" r="6.5" stroke="#a9b4c1"/>
    </g>
    <use href="#i-bldg" x="45" y="80" width="6" height="6"/>
    <use href="#i-doc" x="103" y="55" width="6" height="6"/>
    <use href="#i-team" x="148" y="86" width="6" height="6"/>
    <use href="#i-grow" x="104" y="118" width="6" height="6"/>
    <use href="#i-money" x="58" y="132" width="6" height="6"/>
    <path d="M225 75l3 4-3 4" fill="none" stroke="#2d6fc4" stroke-width="2.4"/>
  </svg>
  <div class="abs lorem" style="left:88px;top:36px;width:42px">Lorem Ipsum is simply dummy text of the printing and typesetting industry.</div>
  <div class="abs lorem" style="left:30px;top:61px;width:42px">Lorem Ipsum is simply dummy text of the printing and typesetting industry.</div>
  <div class="abs lorem" style="left:132px;top:68px;width:42px">Lorem Ipsum is simply dummy text of the printing and typesetting industry.</div>
  <div class="abs lorem" style="left:88px;top:100px;width:42px">Lorem Ipsum is simply dummy text of the printing and typesetting industry.</div>
  <div class="abs lorem" style="left:43px;top:114px;width:42px">Lorem Ipsum is simply dummy text of the printing and typesetting industry.</div>
  <div class="abs" style="left:237px;top:72px;width:48px"><div class="key">Some key messages here in this format</div><div class="key-body">Lorem Ipsum is simply dummy text of the printing and typesetting industry.</div></div>
  <div class="foot"><span class="src">Source here if needed</span><span class="mark"><span class="dot"></span>BRIGHTVALE</span><span class="num">6</span></div>
</section>

<!-- 7 rocket timeline -->
<section class="slide col-l r4">
  <div class="kicker">Infographic layouts</div><div class="rule"></div><div class="conf">STRICTLY CONFIDENTIAL</div>
  <div class="s-title">Timeline/ product launch infographic</div><div class="s-sub">Sample subtitle</div>
  <svg class="layer" width="304" height="171" viewBox="0 0 304 171" style="color:#ffffff">
    <rect x="182" y="19" width="20" height="34" rx="9" fill="#2a5ea8" role="img" aria-label="Rocket illustration launching from the top of the stack"/>
    <polygon points="186,53 198,53 202,70 182,70" fill="#f0df8a"/>
    <polygon points="182,70 202,70 206,87 178,87" fill="#8fb06c"/>
    <polygon points="178,87 206,87 210,104 174,104" fill="#8567b3"/>
    <polygon points="174,104 210,104 214,121 170,121" fill="#5b95d6"/>
    <polygon points="170,121 214,121 218,138 166,138" fill="#6e86c0"/>
    <polygon points="166,138 218,138 222,160 162,160" fill="#a9b4c1"/>
    <use href="#i-team" x="187.5" y="74" width="9" height="9"/>
    <use href="#i-grow" x="187.5" y="91" width="9" height="9"/>
    <use href="#i-money" x="187.5" y="108" width="9" height="9"/>
    <use href="#i-bldg" x="187.5" y="125" width="9" height="9"/>
    <use href="#i-doc" x="187.5" y="144" width="9" height="9"/>
    <g fill="none" stroke="#7b8594" stroke-width=".3">
      <path d="M165 81l8 1 8 -5"/><path d="M157 115l8 1 12 -6"/><path d="M150 147l10 2 10 -6"/>
      <path d="M217 59l6 -5h8"/><path d="M223 93l8 -6h10"/><path d="M230 125l8 -6h10"/>
    </g>
  </svg>
  <div class="abs" style="left:17px;top:77px;width:48px"><div class="key">Some key messages here in this format</div><div class="key-body">Lorem Ipsum is simply dummy text of the printing and typesetting industry.</div></div>
  <div class="abs" style="left:115px;top:62px;width:48px;text-align:right"><div class="hd">Heading here</div><div class="body3">Lorem Ipsum is simply dummy text of the printing and typesetting industry.</div></div>
  <div class="abs" style="left:106px;top:95px;width:48px;text-align:right"><div class="hd">Heading here</div><div class="body3">Lorem Ipsum is simply dummy text of the printing and typesetting industry.</div></div>
  <div class="abs" style="left:99px;top:130px;width:48px;text-align:right"><div class="hd">Heading here</div><div class="body3">Lorem Ipsum is simply dummy text of the printing and typesetting industry.</div></div>
  <div class="abs" style="left:222px;top:49px;width:54px"><div class="hd">Heading here</div><div class="body3">Lorem Ipsum is simply dummy text of the printing and typesetting industry.</div></div>
  <div class="abs" style="left:231px;top:84px;width:54px"><div class="hd">Heading here</div><div class="body3">Lorem Ipsum is simply dummy text of the printing and typesetting industry.</div></div>
  <div class="abs" style="left:238px;top:116px;width:54px"><div class="hd">Heading here</div><div class="body3">Lorem Ipsum is simply dummy text of the printing and typesetting industry.</div></div>
  <div class="foot"><span class="src">Source here if needed</span><span class="mark"><span class="dot"></span>BRIGHTVALE</span><span class="num">7</span></div>
</section>

<!-- 8 arc timeline -->
<section class="slide col-r r4">
  <div class="kicker">Infographic layouts</div><div class="rule"></div><div class="conf">STRICTLY CONFIDENTIAL</div>
  <div class="s-title">Timeline/ product launch infographic</div><div class="s-sub">Sample subtitle</div>
  <svg class="layer" width="304" height="171" viewBox="0 0 304 171">
    <defs><linearGradient id="laptopTone" x1="0" y1="0" x2="0" y2="1"><stop offset="0" stop-color="#c7ced8"/><stop offset="1" stop-color="#e6eaf0"/></linearGradient></defs>
    <path d="M104 155 A 54 54 0 1 1 202 155" fill="none" stroke="#ffffff" stroke-width="1.2"/>
    <g fill="#ffffff" stroke="#5a6576" stroke-width=".6">
      <circle cx="102" cy="131" r="2"/><circle cx="102" cy="85" r="2"/><circle cx="148" cy="62" r="2"/><circle cx="194" cy="84" r="2"/><circle cx="194" cy="131" r="2"/>
    </g>
    <g fill="#ffffff" stroke-width="1.6">
      <circle cx="88" cy="138" r="7" stroke="#3d5a9c"/><circle cx="90" cy="77" r="7" stroke="#2d6fc4"/><circle cx="148" cy="47" r="7" stroke="#8567b3"/><circle cx="206" cy="74" r="7" stroke="#4fe0a0"/><circle cx="209" cy="132" r="7" stroke="#98c98a"/>
    </g>
    <g font-family="Barlow,Arial,sans-serif" font-size="6.5" font-weight="600" fill="#1f4f9a" text-anchor="middle">
      <text x="88" y="140.5">A</text><text x="90" y="79.5">B</text><text x="148" y="49.5">C</text><text x="206" y="76.5">D</text><text x="209" y="134.5">E</text>
    </g>
    <rect x="106" y="110" width="86" height="50" rx="3" fill="url(#laptopTone)" role="img" aria-label="Laptop illustration at the base of the arc"/>
  </svg>
  <div class="abs" style="left:128px;top:84px;width:40px;text-align:center;font-size:4.8px;font-weight:600;line-height:1.2;color:var(--heading-blue)">Main Heading Here</div>
  <div class="abs" style="left:160px;top:36px;width:48px"><div class="hd">Heading here</div><div class="body3">Lorem Ipsum is simply dummy text of the printing and typesetting industry.</div></div>
  <div class="abs" style="left:32px;top:67px;width:48px;text-align:right"><div class="hd">Heading here</div><div class="body3">Lorem Ipsum is simply dummy text of the printing and typesetting industry.</div></div>
  <div class="abs" style="left:218px;top:63px;width:48px"><div class="hd">Heading here</div><div class="body3">Lorem Ipsum is simply dummy text of the printing and typesetting industry.</div></div>
  <div class="abs" style="left:30px;top:128px;width:48px;text-align:right"><div class="hd">Heading here</div><div class="body3">Lorem Ipsum is simply dummy text of the printing and typesetting industry.</div></div>
  <div class="abs" style="left:221px;top:122px;width:48px"><div class="hd">Heading here</div><div class="body3">Lorem Ipsum is simply dummy text of the printing and typesetting industry.</div></div>
  <div class="foot"><span class="src">Source here if needed</span><span class="mark"><span class="dot"></span>BRIGHTVALE</span><span class="num">8</span></div>
</section>

<!-- 9 factoids -->
<section class="slide dark col-l r5">
  <div class="rule"></div><div class="conf">STRICTLY CONFIDENTIAL</div>
  <div class="s-title">Factoids – key numbers</div><div class="s-sub">Subtitle here</div>
  <div class="fact" style="left:17px;top:51px;width:36px"><div class="n">437M</div><div class="t">Lorem Ipsum is simply dummy text of the printing and typesetting industry.</div></div>
  <div class="fact" style="left:76px;top:51px;width:36px"><div class="n">7<small>years</small></div><div class="t">Lorem Ipsum is simply dummy text of the printing and typesetting industry.</div></div>
  <div class="fact" style="left:127px;top:51px;width:36px"><div class="n">+3252</div><div class="t">Lorem Ipsum is simply dummy text of the printing and typesetting industry.</div></div>
  <div class="fact" style="left:195px;top:51px;width:36px"><div class="n">437M</div><div class="t">Lorem Ipsum is simply dummy text of the printing and typesetting industry.</div></div>
  <div class="fact" style="left:253px;top:51px;width:36px"><div class="n">7<small>years</small></div><div class="t">Lorem Ipsum is simply dummy text of the printing and typesetting industry.</div></div>
  <div class="fact" style="left:17px;top:102px;width:36px"><div class="n">3+</div><div class="t">Lorem Ipsum is simply dummy text of the printing and typesetting industry.</div></div>
  <div class="fact" style="left:76px;top:102px;width:36px"><div class="n">17+</div><div class="t">Lorem Ipsum is simply dummy text of the printing and typesetting industry.</div></div>
  <div class="fact" style="left:127px;top:102px;width:55px"><div class="n">4 <small>employees</small></div><div class="t">Lorem Ipsum is simply dummy text of the printing and typesetting industry.</div></div>
  <div class="fact" style="left:195px;top:102px;width:36px"><div class="n">3+</div><div class="t">Lorem Ipsum is simply dummy text of the printing and typesetting industry.</div></div>
  <div class="fact" style="left:253px;top:102px;width:36px"><div class="n">17+</div><div class="t">Lorem Ipsum is simply dummy text of the printing and typesetting industry.</div></div>
  <div class="foot"><span class="src">Source here if needed</span><span class="mark"><span class="dot"></span>BRIGHTVALE</span><span class="num">9</span></div>
</section>

<!-- 10 key content -->
<section class="slide col-r r5">
  <div class="kicker">Infographic layouts</div><div class="rule"></div><div class="conf">STRICTLY CONFIDENTIAL</div>
  <div class="s-title">Key Content infographic</div><div class="s-sub">Sample subtitle</div>
  <svg class="layer" width="304" height="171" viewBox="0 0 304 171" style="color:#1b2433">
    <circle cx="41" cy="55" r="10" fill="#5b95d6"/><circle cx="41" cy="95" r="10" fill="#98c98a"/><circle cx="41" cy="135" r="10" fill="#4fe0a0"/>
    <circle cx="136" cy="55" r="10" fill="#8567b3"/><circle cx="136" cy="95" r="10" fill="#6e86c0"/><circle cx="136" cy="135" r="10" fill="#5b95d6"/>
    <circle cx="232" cy="55" r="10" fill="#98c98a"/><circle cx="232" cy="95" r="10" fill="#4fe0a0"/><circle cx="232" cy="135" r="10" fill="#a99bd0"/>
    <g fill="#ffffff">
      <circle cx="39" cy="55" r="4.5"/><circle cx="39" cy="95" r="4.5"/><circle cx="39" cy="135" r="4.5"/>
      <circle cx="134" cy="55" r="4.5"/><circle cx="134" cy="95" r="4.5"/><circle cx="134" cy="135" r="4.5"/>
      <circle cx="230" cy="55" r="4.5"/><circle cx="230" cy="95" r="4.5"/><circle cx="230" cy="135" r="4.5"/>
    </g>
    <g font-family="Barlow,Arial,sans-serif" font-size="5" font-weight="600" fill="#1b2433" text-anchor="middle">
      <text x="39" y="56.8">1</text><text x="39" y="96.8">2</text><text x="39" y="136.8">3</text>
      <text x="134" y="56.8">4</text><text x="134" y="96.8">5</text><text x="134" y="136.8">6</text>
      <text x="230" y="56.8">7</text><text x="230" y="96.8">8</text><text x="230" y="136.8">9</text>
    </g>
    <use href="#i-doc" x="16" y="50" width="10" height="10"/><use href="#i-doc" x="16" y="90" width="10" height="10"/><use href="#i-doc" x="16" y="130" width="10" height="10"/>
    <use href="#i-doc" x="111" y="50" width="10" height="10"/><use href="#i-doc" x="111" y="90" width="10" height="10"/><use href="#i-doc" x="111" y="130" width="10" height="10"/>
    <use href="#i-doc" x="207" y="50" width="10" height="10"/><use href="#i-doc" x="207" y="90" width="10" height="10"/><use href="#i-doc" x="207" y="130" width="10" height="10"/>
  </svg>
  <div class="abs" style="left:55px;top:45px;width:45px"><div class="hd">Heading here</div><div class="body3">Lorem Ipsum is simply dummy text of the printing and typesetting industry.</div></div>
  <div class="abs" style="left:55px;top:85px;width:45px"><div class="hd">Heading here</div><div class="body3">Lorem Ipsum is simply dummy text of the printing and typesetting industry.</div></div>
  <div class="abs" style="left:55px;top:125px;width:45px"><div class="hd">Heading here</div><div class="body3">Lorem Ipsum is simply dummy text of the printing and typesetting industry.</div></div>
  <div class="abs" style="left:150px;top:45px;width:45px"><div class="hd">Heading here</div><div class="body3">Lorem Ipsum is simply dummy text of the printing and typesetting industry.</div></div>
  <div class="abs" style="left:150px;top:85px;width:45px"><div class="hd">Heading here</div><div class="body3">Lorem Ipsum is simply dummy text of the printing and typesetting industry.</div></div>
  <div class="abs" style="left:150px;top:125px;width:45px"><div class="hd">Heading here</div><div class="body3">Lorem Ipsum is simply dummy text of the printing and typesetting industry.</div></div>
  <div class="abs" style="left:246px;top:45px;width:45px"><div class="hd">Heading here</div><div class="body3">Lorem Ipsum is simply dummy text of the printing and typesetting industry.</div></div>
  <div class="abs" style="left:246px;top:85px;width:45px"><div class="hd">Heading here</div><div class="body3">Lorem Ipsum is simply dummy text of the printing and typesetting industry.</div></div>
  <div class="abs" style="left:246px;top:125px;width:45px"><div class="hd">Heading here</div><div class="body3">Lorem Ipsum is simply dummy text of the printing and typesetting industry.</div></div>
  <div class="foot"><span class="src">Source here if needed</span><span class="mark"><span class="dot"></span>BRIGHTVALE</span><span class="num">10</span></div>
</section>

<!-- 11 goal -->
<section class="slide col-l r6">
  <div class="kicker">Infographic layouts</div><div class="rule"></div><div class="conf">STRICTLY CONFIDENTIAL</div>
  <div class="s-title">Goal infographic</div><div class="s-sub">Sample subtitle</div>
  <svg class="layer" width="304" height="171" viewBox="0 0 304 171">
    <defs><linearGradient id="goalTone" x1="0" y1="0" x2="0" y2="1"><stop offset="0" stop-color="#4fa8d8"/><stop offset="1" stop-color="#1f4f9a"/></linearGradient></defs>
    <g role="img" aria-label="Arrow striking a target illustration in blue tones">
      <rect x="182" y="24" width="6" height="122" rx="3" fill="url(#goalTone)"/>
      <ellipse cx="185" cy="150" rx="48" ry="11" fill="url(#goalTone)"/>
    </g>
    <g stroke="#7b8594" stroke-width=".3" fill="none">
      <line x1="163" y1="54" x2="182" y2="54"/><line x1="140" y1="77" x2="182" y2="77"/><line x1="163" y1="104" x2="182" y2="104"/>
      <line x1="188" y1="61" x2="207" y2="61"/><line x1="188" y1="88" x2="229" y2="88"/><line x1="188" y1="108" x2="207" y2="108"/>
    </g>
    <g stroke="#ffffff" stroke-width=".6">
      <circle cx="162" cy="54" r="1.6" fill="#3d2a6a"/><circle cx="139" cy="77" r="1.6" fill="#e8c24a"/><circle cx="162" cy="104" r="1.6" fill="#4fe0a0"/>
      <circle cx="208" cy="61" r="1.6" fill="#2d6fc4"/><circle cx="230" cy="88" r="1.6" fill="#1b2d5a"/><circle cx="208" cy="108" r="1.6" fill="#4fe0a0"/>
    </g>
  </svg>
  <div class="abs" style="left:17px;top:74px;width:48px"><div class="key">Some key messages here in this format</div><div class="key-body">Lorem Ipsum is simply dummy text of the printing and typesetting industry.</div></div>
  <div class="abs" style="left:108px;top:40px;width:50px;text-align:right"><div class="hd">Heading here</div><div class="body3">Lorem Ipsum is simply dummy text of the printing and typesetting industry.</div></div>
  <div class="abs" style="left:85px;top:68px;width:50px;text-align:right"><div class="hd">Heading here</div><div class="body3">Lorem Ipsum is simply dummy text of the printing and typesetting industry.</div></div>
  <div class="abs" style="left:108px;top:95px;width:50px;text-align:right"><div class="hd">Heading here</div><div class="body3">Lorem Ipsum is simply dummy text of the printing and typesetting industry.</div></div>
  <div class="abs" style="left:214px;top:46px;width:50px"><div class="hd">Heading here</div><div class="body3">Lorem Ipsum is simply dummy text of the printing and typesetting industry.</div></div>
  <div class="abs" style="left:236px;top:74px;width:50px"><div class="hd">Heading here</div><div class="body3">Lorem Ipsum is simply dummy text of the printing and typesetting industry.</div></div>
  <div class="abs" style="left:214px;top:103px;width:50px"><div class="hd">Heading here</div><div class="body3">Lorem Ipsum is simply dummy text of the printing and typesetting industry.</div></div>
  <div class="foot"><span class="src">Source here if needed</span><span class="mark"><span class="dot"></span>BRIGHTVALE</span><span class="num">11</span></div>
</section>

<!-- 12 thank you -->
<section class="slide thanks col-r r6">
  <svg class="layer" width="304" height="171" viewBox="0 0 304 171" role="img" aria-label="City skyline photograph in navy and blue behind diagonal panels">
    <defs><linearGradient id="thanksSky" x1="0" y1="0" x2="1" y2="1"><stop offset="0" stop-color="#2a3f6e"/><stop offset="1" stop-color="#3f6aa6"/></linearGradient></defs>
    <rect width="304" height="171" fill="url(#thanksSky)"/>
    <polygon points="0,0 210,0 170,100 0,100" fill="#1b2d5a" opacity=".75"/>
    <polygon points="0,100 170,100 135,171 0,171" fill="#1b2d5a" opacity=".9"/>
    <polygon points="230,0 304,0 304,120 220,171 160,171" fill="#2f6fc4" opacity=".55"/>
    <polygon points="250,171 275,150 304,140 304,171" fill="#2f7fd8"/>
    <polygon points="240,171 255,160 262,171" fill="#7aa33a"/>
  </svg>
  <div class="msg">Thank you.</div>
  <div class="brand"><span class="dot"></span>BRIGHTVALE</div>
</section>

</body>
</html>
```